Business Card Design for Kestrelwood Carpentry

I need a business card design for my carpentry company Kestrelwood Carpentry. Ive attached files with all information I require on both sides. Look forward to seeing your design.

```html
<!DOCTYPE html>
<html lang="en">
<head>
<meta charset="utf-8">
<title>Kestrelwood Carpentry – Business Card</title>
<link href="https://fonts.googleapis.com/css2?family=Exo+2:wght@400;600;800&family=Orbitron:wght@700&display=swap" rel="stylesheet">
<style>
  :root{
    --orange:#f0592b;
    --ink:#1c1c1c;
    --paper:#ffffff;
    --grey:#e4e4e4;
    --grey-dark:#c9c9c9;
    --backdrop:#f2f2f2;
  }
  *{box-sizing:border-box;margin:0;padding:0}
  html,body{width:1200px;height:1200px;overflow:hidden;background:var(--backdrop)}
  body{position:relative;font-family:"Exo 2",sans-serif;color:var(--ink)}

  .card{position:absolute;left:120px;width:960px;height:540px;overflow:hidden;box-shadow:0 6px 18px rgba(0,0,0,.12)}
  .card--front{top:40px;background:var(--paper)}
  .card--back{top:620px;background:var(--orange)}

  /* front */
  .brand{position:absolute;left:0;right:0;top:110px;display:flex;justify-content:center;align-items:center;gap:18px}
  .brand__dot{width:22px;height:22px;border-radius:50%;background:var(--orange)}
  .brand__name{font-family:"Exo 2",sans-serif;font-weight:800;font-size:58px;letter-spacing:3px;color:var(--ink);text-transform:uppercase}
  .phone{position:absolute;left:0;right:0;top:240px;display:flex;justify-content:center;align-items:center;gap:26px}
  .phone__icon{width:64px;height:64px}
  .phone__number{font-family:"Orbitron",sans-serif;font-weight:700;font-size:72px;letter-spacing:2px;color:var(--ink)}
  .tagline-row{position:absolute;left:0;right:0;top:400px;display:flex;align-items:center;gap:24px}
  .rule-pair{flex:1;display:flex;flex-direction:column;gap:8px}
  .rule-pair span{display:block;height:4px;background:var(--orange)}
  .tagline{font-family:"Exo 2",sans-serif;font-weight:600;font-size:34px;color:var(--orange);white-space:nowrap}

  /* back */
  .back__band{position:absolute;left:0;right:0;top:70px;height:46px;background:var(--grey);border-bottom:3px solid var(--grey-dark)}
  .back__band::after{content:"";position:absolute;left:0;right:0;top:16px;height:3px;background:var(--orange)}
  .back__tab{position:absolute;left:130px;top:0;width:330px;height:140px;background:var(--grey);border-radius:0 0 22px 22px;border:3px solid var(--grey-dark);border-top:0;display:flex;align-items:center;justify-content:center;gap:10px;z-index:1}
  .back__tab .brand__name{font-size:28px;letter-spacing:1px}
  .back__tab .brand__dot{width:12px;height:12px}
  .services{position:absolute;left:0;right:0;top:180px;text-align:center;list-style:none;color:var(--paper);font-size:27px;line-height:48px;letter-spacing:.5px}
  .services li::before{content:"• "}
  .back__footer{position:absolute;left:0;right:0;top:420px;height:54px;background:var(--grey);display:flex;align-items:center;justify-content:space-between;padding:0 60px;font-size:24px;color:var(--ink)}
  .back__rule{position:absolute;left:0;right:0;top:488px;height:4px;background:var(--grey)}
  .licence{font-family:"Orbitron",sans-serif;font-weight:700;font-size:22px;letter-spacing:1px}
</style>
</head>
<body>

<section class="card card--front" aria-label="Card front">
  <div class="brand">
    <span class="brand__dot"></span>
    <span class="brand__name">Kestrelwood Carpentry</span>
  </div>
  <div class="phone">
    <svg class="phone__icon" viewBox="0 0 64 64" aria-hidden="true">
      <path d="M8 40 C8 52 20 58 32 58 C44 58 56 52 56 40 L44 36 L40 44 C34 44 30 44 24 44 L20 36 Z" fill="#1c1c1c"/>
      <path d="M22 24 A14 14 0 0 1 42 24" stroke="#1c1c1c" stroke-width="4" fill="none" stroke-linecap="round"/>
      <path d="M15 17 A24 24 0 0 1 49 17" stroke="#1c1c1c" stroke-width="4" fill="none" stroke-linecap="round"/>
    </svg>
    <span class="phone__number">0491570110</span>
  </div>
  <div class="tagline-row">
    <div class="rule-pair"><span></span><span></span></div>
    <p class="tagline">Anything Carpentry, Anywhere in Sydney</p>
    <div class="rule-pair"><span></span><span></span></div>
  </div>
</section>

<section class="card card--back" aria-label="Card back">
  <div class="back__band"></div>
  <div class="back__tab">
    <span class="brand__dot"></span>
    <span class="brand__name">Kestrelwood Carpentry</span>
  </div>
  <ul class="services">
    <li>Decks &amp; Pergolas • Shop Fitouts • Wall &amp; Roof Framing</li>
    <li>Refurbishments • Doors &amp; Windows • Fences &amp; Gates</li>
    <li>Attic Conversions • Privacy Screens • Timber Flooring</li>
    <li>Wall Cladding • Extensions and more</li>
  </ul>
  <div class="back__footer">
    <span class="licence">Lic #918305B</span>
    <span class="email">kestrelwoodcarpentry@mail.com</span>
  </div>
  <div class="back__rule"></div>
</section>

</body>
</html>
```